Business card design for Tolvin Waste

I would like double-sided business cards for myself and my partner that includes our logo and the existing colour scheme. We provide waste and environmental services to customers in the motor-vehicle and engineering industries.

```html
<!DOCTYPE html>
<html lang="en">
<head>
<meta charset="utf-8">
<title>Tolvin Waste – Business Cards</title>
<link rel="stylesheet" href="https://fonts.googleapis.com/css2?family=Montserrat:wght@600&family=Roboto:wght@400;500&display=swap">
<style>
  :root {
    --backdrop: #d6e8ee;
    --charcoal: #4b4b4b;
    --paper: #ffffff;
    --leaf: #6aa53f;
    --leaf-dark: #4f7f2d;
    --lime: #8cc63f;
    --ink: #2c2c2c;
    --light-text: #f2f2f2;
  }
  * { margin: 0; padding: 0; box-sizing: border-box; }
  html, body { width: 1200px; height: 900px; overflow: hidden; }
  body {
    background: var(--backdrop);
    font-family: "Roboto", Arial, sans-serif;
    position: relative;
  }
  .card {
    position: absolute;
    left: 280px;
    width: 640px;
    height: 366px;
    border-radius: 18px;
    overflow: hidden;
    box-shadow: 0 6px 18px rgba(0,0,0,.18);
  }
  .card--back { top: 60px; background: var(--charcoal); }
  .card--front { top: 474px; background: var(--paper); }

  .brand {
    position: absolute;
    display: flex;
    align-items: center;
    gap: 14px;
  }
  .brand__dot {
    border-radius: 50%;
    background: var(--lime);
    flex: none;
  }
  .brand__name {
    font-family: "Montserrat", Arial, sans-serif;
    font-weight: 600;
    text-transform: uppercase;
    letter-spacing: .04em;
    white-space: nowrap;
  }
  .card--back .brand { left: 50%; top: 150px; transform: translateX(-50%); }
  .card--back .brand__dot { width: 54px; height: 54px; }
  .card--back .brand__name { color: var(--paper); font-size: 44px; }

  .website-line {
    position: absolute;
    bottom: 34px;
    width: 100%;
    text-align: center;
    color: var(--light-text);
    font-size: 15px;
    letter-spacing: .02em;
  }

  .front-art { position: absolute; inset: 0; }

  .card--front .brand { left: 40px; top: 140px; gap: 10px; }
  .card--front .brand__dot { width: 30px; height: 30px; }
  .card--front .brand__name { color: var(--charcoal); font-size: 22px; }

  .holder {
    position: absolute;
    left: 293px;
    top: 48px;
    width: 260px;
    color: var(--paper);
    text-align: center;
  }
  .holder__name { font-size: 20px; font-weight: 500; letter-spacing: .02em; }
  .holder__role { font-size: 12px; margin-top: 3px; }

  .contacts {
    position: absolute;
    left: 40px;
    bottom: 34px;
    list-style: none;
  }
  .contacts li {
    display: flex;
    align-items: center;
    gap: 14px;
    height: 28px;
    font-size: 16px;
    color: var(--ink);
  }
  .contacts__icon {
    width: 22px; height: 22px;
    background: var(--lime);
    display: flex; align-items: center; justify-content: center;
  }
  .contacts__icon svg { width: 14px; height: 14px; fill: var(--paper); }

  .address {
    position: absolute;
    right: 34px;
    bottom: 70px;
    width: 220px;
    text-align: center;
    color: var(--light-text);
    font-size: 15px;
    line-height: 1.35;
  }
  .address svg { width: 14px; height: 18px; fill: var(--paper); display: block; margin: 0 auto 8px; }
</style>
</head>
<body>

  <section class="card card--back" aria-label="Card back">
    <div class="brand">
      <span class="brand__dot"></span>
      <span class="brand__name">Tolvin Waste</span>
    </div>
    <p class="website-line">www.tolvinwaste.com</p>
  </section>

  <section class="card card--front" aria-label="Card front">
    <svg class="front-art" viewBox="0 0 640 366" width="640" height="366" aria-hidden="true">
      <defs>
        <linearGradient id="fold-shade" x1="0" x2="1" y1="0" y2="0">
          <stop offset="0" stop-color="#000" stop-opacity="0"/>
          <stop offset="1" stop-color="#000" stop-opacity=".22"/>
        </linearGradient>
      </defs>
      <polygon points="262,0 280,0 370,366 352,366" fill="url(#fold-shade)"/>
      <polygon class="dark-panel" points="280,0 640,0 640,366 370,366" fill="#4b4b4b"/>
      <polygon class="ribbon-fold" points="266,104 300,104 300,124" fill="#4f7f2d"/>
      <rect class="ribbon" x="266" y="40" width="314" height="64" fill="#6aa53f"/>
    </svg>

    <div class="brand">
      <span class="brand__dot"></span>
      <span class="brand__name">Tolvin Waste</span>
    </div>

    <div class="holder">
      <p class="holder__name">MAREK OLSEN</p>
      <p class="holder__role">Founder &amp; Director</p>
    </div>

    <ul class="contacts">
      <li><span class="contacts__icon"><svg viewBox="0 0 24 24"><path d="M6.6 10.8a15 15 0 0 0 6.6 6.6l2.2-2.2c.3-.3.7-.4 1-.2 1.1.4 2.3.6 3.6.6.6 0 1 .4 1 1V20c0 .6-.4 1-1 1A17 17 0 0 1 3 4c0-.6.4-1 1-1h3.5c.6 0 1 .4 1 1 0 1.3.2 2.5.6 3.6.1.3 0 .7-.2 1z"/></svg></span>555-210-4471</li>
      <li><span class="contacts__icon"><svg viewBox="0 0 24 24"><path d="M3 8c0-2 4-4 9-4s9 2 9 4v2h-5V8H8v2H3zM6 11h12l2 9H4zm6 2a3 3 0 1 0 0 6 3 3 0 0 0 0-6z"/></svg></span>555-318-2290</li>
      <li><span class="contacts__icon"><svg viewBox="0 0 24 24"><path d="M2 5h20v14H2zm2 2v.5l8 5.5 8-5.5V7zm0 3v7h16v-7l-8 5.5z"/></svg></span>hello@tolvinwaste.com</li>
      <li><span class="contacts__icon"><svg viewBox="0 0 24 24"><path d="M12 2a10 10 0 1 0 0 20 10 10 0 0 0 0-20zm0 2c1.2 1.4 2 3.4 2.3 5.5H9.7C10 7.4 10.8 5.4 12 4zM4.3 13.5a8 8 0 0 1 0-3h3.4a17 17 0 0 0 0 3zm5.4 0a15 15 0 0 1 0-3h4.6a15 15 0 0 1 0 3zm6.6 0a17 17 0 0 0 0-3h3.4a8 8 0 0 1 0 3zM12 20c-1.2-1.4-2-3.4-2.3-5.5h4.6C14 16.6 13.2 18.6 12 20z"/></svg></span>www.tolvinwaste.com</li>
    </ul>

    <div class="address">
      <svg viewBox="0 0 24 32"><path d="M12 0a11 11 0 0 0-11 11c0 8 11 21 11 21s11-13 11-21A11 11 0 0 0 12 0zm0 15a4 4 0 1 1 0-8 4 4 0 0 1 0 8z"/></svg>
      48 Harbour Road - Millbrook<br>Westvale 20418
    </div>
  </section>

</body>
</html>
```